Business Card & Word Docs from existing Logo

We need a business card with typical information plus layout to include electrical contractors license number, VONEL license and KMP license. We would like a word document layout for a proposal document, opening page with logo and design basic information; proposal to and proposal from and project name and number. Small basic single page letter for general documents. Email signature with logo.

We are an electrical, refrigeration and automation contractor. We work with reducing energy consumption for our customers and complex process solutions in electrical, refrigeration and automation.

Reason: Final changes/ revisions to designs.

Target Market(s)

Industrial and commercial businesses that require more than your average contractor.

Industry/Entity Type

Electrical

Requirements
Must have
• Propsal document must have a full opening page.

```html
<!DOCTYPE html>
<html lang="en">
<head>
<meta charset="utf-8">
<title>Polarline Contracting – Business Card</title>
<link href="https://fonts.googleapis.com/css2?family=Arimo:wght@400;700&display=swap" rel="stylesheet">
<style>
  :root {
    --page: #ffffff;
    --brand-blue: #1f86b8;
    --brand-green: #22a052;
    --ink: #1d1d1f;
    --white: #ffffff;
  }
  html, body {
    margin: 0;
    width: 1200px;
    height: 900px;
    overflow: hidden;
    background: var(--page);
    font-family: "Arimo", Arial, sans-serif;
  }
  .card {
    position: absolute;
    left: 98px;
    top: 137px;
    width: 1004px;
    height: 626px;
    background: var(--white);
    box-shadow: 0 14px 40px rgba(0,0,0,0.28);
    overflow: hidden;
  }
  .card__header {
    position: absolute;
    inset: 0 0 auto 0;
    height: 310px;
    background:
      linear-gradient(to bottom, rgba(255,255,255,0) 35%, rgba(255,255,255,0.85) 85%, #fff 100%),
      linear-gradient(115deg, #1f8a58 0%, #2e7f86 22%, #3a86a8 45%, #2a72b8 70%, #3f94d4 100%);
  }
  .logo-panel {
    position: absolute;
    left: 0;
    top: 41px;
    width: 547px;
    height: 157px;
    background: var(--white);
    border-radius: 0 20px 20px 0;
  }
  .logo-panel__mark {
    position: absolute;
    left: 50px;
    top: 22px;
  }
  .logo-panel__name {
    position: absolute;
    left: 192px;
    top: 32px;
    margin: 0;
    color: var(--brand-blue);
    font-weight: 700;
    font-size: 41px;
    line-height: 47px;
    letter-spacing: 1px;
  }
  .person {
    position: absolute;
    right: 60px;
    top: 56px;
    text-align: right;
    color: var(--white);
  }
  .person__name { margin: 0; font-weight: 700; font-size: 39px; line-height: 46px; }
  .person__role { margin: 0; font-size: 35px; line-height: 46px; }
  .details {
    position: absolute;
    top: 306px;
    font-size: 31px;
    line-height: 40px;
    color: var(--ink);
  }
  .details p { margin: 0; white-space: nowrap; }
  .details .label { color: var(--brand-blue); font-weight: 700; }
  .details--web { right: 384px; text-align: right; }
  .details--web .gap { height: 38px; }
  .details--phone { right: 67px; }
  .details--phone .label { display: inline-block; width: 40px; text-align: right; margin-right: 8px; }
  .card__footer {
    position: absolute;
    left: 0;
    bottom: 0;
    width: 100%;
    height: 79px;
    background: linear-gradient(100deg, #23864f 0%, #2a7a88 35%, #2360a0 65%, #3a8fd0 100%);
    color: var(--white);
    font-size: 31px;
    line-height: 79px;
    text-align: center;
    word-spacing: 3px;
  }
</style>
</head>
<body>
  <div class="card">
    <div class="card__header"></div>

    <div class="logo-panel">
      <svg class="logo-panel__mark" width="120" height="120" viewBox="0 0 120 120" aria-hidden="true">
        <circle cx="60" cy="60" r="58" fill="#22a052"/>
      </svg>
      <p class="logo-panel__name">POLARLINE<br>CONTRACTING</p>
    </div>

    <div class="person">
      <p class="person__name">Sam Carter</p>
      <p class="person__role">Director</p>
    </div>

    <div class="details details--web">
      <p><span class="label">E-mail</span>&nbsp;&nbsp; sam@polarline.com.au</p>
      <p><span class="label">Website</span>&nbsp; www.polarline.com.au</p>
      <div class="gap"></div>
      <p><span class="label">Electrical Contractors License</span> 12345</p>
      <p><span class="label">KMP</span> 1234567 &nbsp;|&nbsp; <span class="label">VONEL</span> AA12345</p>
    </div>

    <div class="details details--phone">
      <p><span class="label">T:</span>07 5550 1820</p>
      <p><span class="label">F:</span>07 5550 1821</p>
      <p><span class="label">M:</span>0400 555 182</p>
    </div>

    <div class="card__footer">PO Box 880 &nbsp;•&nbsp; Harbourside &nbsp;•&nbsp; Queensland &nbsp;•&nbsp; 4801</div>
  </div>
</body>
</html>
```